Commercial Landscaping Flyer Needed

Looking for a flyer design to showcase what we offer for commercial landscape Installations. We want this to illustrate what sets us apart from our competitors. Include our EMR Safety rating of .72, that our average commercial landscape installation size is $215,000 with our largest completed in 2020 being $1,375,590. We have backgrounds in commercial design and installation and help our customers with Value Engineering Strategies. Since incorporating in 2005, we have an average employment retention length of 8 years. We want this flyer to show our commercial clients that we mean business and are dedicated to making their project happen on time, run efficiently, and we do excellent work.

Need extra days to review

```html
<!DOCTYPE html>
<html lang="en">
<head>
<meta charset="UTF-8">
<title>Commercial Landscape Installations Flyer</title>
<link href="https://fonts.googleapis.com/css2?family=Open+Sans:wght@300;400;600;700;800&family=Oswald:wght@600;700&display=swap" rel="stylesheet">
<style>
  :root {
    --lime: #c3d82e;
    --lime-dark: #a9bf1c;
    --ink: #141414;
    --paper: #ffffff;
    --backdrop: #e6e6e6;
    --text: #1d1d1d;
  }
  * { box-sizing: border-box; margin: 0; padding: 0; }
  html, body {
    width: 1200px; height: 2191px; overflow: hidden;
    background: var(--backdrop);
    font-family: "Open Sans", Arial, sans-serif;
    color: var(--text);
  }
  .flyer {
    position: absolute; left: 37px; top: 299px;
    width: 1126px; height: 1593px;
    background: var(--paper);
    box-shadow: 0 10px 40px rgba(0,0,0,.18);
    overflow: hidden;
  }
  .accent-bar { position: absolute; background: var(--lime); }
  .accent-bar--top { left: 415px; top: 0; width: 296px; height: 21px; }
  .accent-bar--bottom { left: 786px; bottom: 0; width: 260px; height: 22px; }

  .headline {
    position: absolute; left: 0; top: 72px; width: 100%;
    text-align: center; font-size: 62px; line-height: 66px;
    text-transform: uppercase; letter-spacing: 0.5px;
  }
  .headline .light { font-weight: 300; color: var(--ink); }
  .headline .green { font-weight: 800; color: var(--lime); }
  .headline .bold { font-weight: 800; color: var(--ink); }

  .intro {
    position: absolute; left: 0; top: 218px; width: 100%;
    text-align: center; font-size: 25px; line-height: 36px; color: var(--ink);
  }
  .intro strong { font-weight: 700; }

  .hero-photo {
    position: absolute; left: 0; top: 327px; width: 100%; height: 525px;
    background:
      radial-gradient(ellipse at 60% 55%, #b9a28a 0%, rgba(185,162,138,0) 38%),
      radial-gradient(ellipse at 40% 75%, #4f7d2c 0%, rgba(79,125,44,0) 40%),
      linear-gradient(90deg, #3d3d36 0%, #c9b62a 12%, #4a5a33 26%, #6f8a3e 45%, #9a8f7d 62%, #3e5a2a 80%, #56625a 100%);
  }

  .stats-band {
    position: absolute; left: 0; top: 852px; width: 100%; height: 213px;
    background: var(--lime);
  }
  .safety-badge {
    position: absolute; left: 245px; top: 810px; width: 635px; height: 78px;
    background: var(--ink); color: #fff;
    font-family: "Oswald", "Arial Narrow", sans-serif; font-weight: 700;
    font-size: 54px; line-height: 78px; text-align: center;
  }
  .safety-badge .green { color: var(--lime); }
  .stat-text {
    position: absolute; top: 928px; width: 500px;
    font-size: 23px; line-height: 31px; color: var(--ink);
  }
  .stat-text strong { font-weight: 700; }
  .stat-text--left { left: 54px; }
  .stat-text--right { left: 587px; }

  .services-title {
    position: absolute; left: 55px; top: 1088px; width: 656px;
    display: flex; align-items: center; gap: 18px;
    font-weight: 800; font-size: 38px; line-height: 48px; color: var(--ink);
  }
  .services-title::before, .services-title::after {
    content: ""; flex: 1; height: 2px;
    background: linear-gradient(90deg, rgba(195,216,46,0), var(--lime));
  }
  .services-title::after { background: linear-gradient(90deg, var(--lime), rgba(195,216,46,0)); }

  .service {
    position: absolute; width: 210px; text-align: center;
    font-size: 18px; line-height: 24px; color: var(--ink);
  }
  .service__photo {
    display: block; width: 210px; height: 147px;
    border: 3px solid var(--lime); margin-bottom: 12px;
  }
  .photo--mowing { background: linear-gradient(160deg, #3d7a22, #7bb03a 50%, #2f6a1b); }
  .photo--turf { background: radial-gradient(circle, #6fb33a, #3f8a22); }
  .photo--hardscape { background: linear-gradient(170deg, #5f6e45, #a29a88 55%, #6b6a5c); }
  .photo--building { background: linear-gradient(180deg, #b9cfe0 0%, #b6a88c 40%, #8a7c63 70%, #4f8a2e 100%); }
  .photo--flowers { background: radial-gradient(circle at 45% 70%, #e9a5b8, rgba(233,165,184,0) 30%), linear-gradient(160deg, #4f7a2c, #b86b3f 55%, #3e6b25); }
  .photo--sprinkler { background: radial-gradient(circle at 65% 40%, #e7eee6, rgba(231,238,230,0) 35%), linear-gradient(160deg, #6b9a3a, #9cbf4e 55%, #4f7d2c); }

  .brand {
    position: absolute; left: 742px; top: 1218px; width: 350px;
    display: flex; align-items: center; justify-content: center; gap: 12px;
  }
  .brand__dot { width: 44px; height: 44px; border-radius: 50%; background: var(--lime); flex: none; }
  .brand__name { font-weight: 700; font-size: 30px; line-height: 36px; color: var(--ink); }

  .quote-title {
    position: absolute; left: 742px; top: 1362px; width: 350px; text-align: center;
    font-family: "Oswald", "Arial Narrow", sans-serif; font-weight: 700;
    font-size: 40px; line-height: 52px; color: var(--ink);
  }
  .phone-pill {
    position: absolute; left: 739px; top: 1422px; width: 353px; height: 38px;
    display: flex; border: 2px solid var(--ink); border-radius: 19px; overflow: hidden;
    font-family: "Oswald", "Arial Narrow", sans-serif; font-weight: 600; font-size: 20px;
  }
  .phone-pill__item {
    flex: 1; display: flex; align-items: center; justify-content: center; gap: 6px;
  }
  .phone-pill__item--dark { background: var(--ink); color: #fff; border-radius: 0 19px 19px 0; }
  .phone-pill__item--light { background: var(--lime); color: var(--ink); }
  .phone-pill svg { width: 14px; height: 14px; }
  .website {
    position: absolute; left: 742px; top: 1476px; width: 350px;
    display: flex; align-items: center; justify-content: center; gap: 8px;
    font-size: 26px; line-height: 34px; color: var(--ink);
  }
  .website .green { color: var(--lime); font-weight: 600; }
  .website svg { width: 16px; height: 16px; }
</style>
</head>
<body>
<main class="flyer">
  <div class="accent-bar accent-bar--top"></div>

  <h1 class="headline">
    <span class="light">We offer</span> <span class="green">Commercial</span><br>
    <span class="green">Landscape</span> <span class="bold">Installations</span>
  </h1>
  <p class="intro">Since incorporating in <strong>2005</strong>, we have an average employment<br>retention length of <strong>8 years.</strong></p>

  <div class="hero-photo" role="img" aria-label="Aerial view of a landscaped apartment courtyard with lawn, paving and seating areas"></div>

  <section class="stats-band"></section>
  <div class="safety-badge"><span class="green">EMR</span> Safety rating of <span class="green">.72</span></div>
  <p class="stat-text stat-text--left">our average commercial landscape installation size is <strong>$215,000</strong> with our largest completed in 2020 being <strong>$1,375,590.</strong></p>
  <p class="stat-text stat-text--right">We have backgrounds in <strong>commercial design</strong> and <strong>installation</strong> and help our customers with Value Engineering Strategies.</p>

  <h2 class="services-title">SERVICES</h2>

  <div class="service" style="left:48px;top:1158px"><span class="service__photo photo--mowing" role="img" aria-label="Striped lawn being mowed with a ride-on mower"></span>Maintenance</div>
  <div class="service" style="left:278px;top:1158px"><span class="service__photo photo--turf" role="img" aria-label="Close-up of healthy green turf"></span>Turf Management</div>
  <div class="service" style="left:507px;top:1158px"><span class="service__photo photo--hardscape" role="img" aria-label="Stone path and boulder garden"></span>Hardscaping</div>
  <div class="service" style="left:48px;top:1358px"><span class="service__photo photo--building" role="img" aria-label="Historic stone building with manicured lawn"></span>Chemical Applications<br>&amp; Fertilization</div>
  <div class="service" style="left:278px;top:1358px"><span class="service__photo photo--flowers" role="img" aria-label="Garden bed with pink hibiscus flowers"></span>Landscaping</div>
  <div class="service" style="left:507px;top:1358px"><span class="service__photo photo--sprinkler" role="img" aria-label="Lawn sprinkler watering grass"></span>Irrigation</div>

  <div class="brand">
    <span class="brand__dot"></span>
    <span class="brand__name">Greenfield Grounds</span>
  </div>

  <div class="quote-title">GET A QUOTE</div>
  <div class="phone-pill">
    <span class="phone-pill__item phone-pill__item--dark">
      <svg viewBox="0 0 24 24"><path fill="#c3d82e" d="M6.6 10.8a15 15 0 0 0 6.6 6.6l2.2-2.2a1 1 0 0 1 1-.25 11.4 11.4 0 0 0 3.6.57 1 1 0 0 1 1 1V20a1 1 0 0 1-1 1A17 17 0 0 1 3 4a1 1 0 0 1 1-1h3.5a1 1 0 0 1 1 1c0 1.25.2 2.45.57 3.6a1 1 0 0 1-.25 1z"/></svg>
      (555) 014-2280
    </span>
    <span class="phone-pill__item phone-pill__item--light">
      <svg viewBox="0 0 24 24"><path fill="#141414" d="M6.6 10.8a15 15 0 0 0 6.6 6.6l2.2-2.2a1 1 0 0 1 1-.25 11.4 11.4 0 0 0 3.6.57 1 1 0 0 1 1 1V20a1 1 0 0 1-1 1A17 17 0 0 1 3 4a1 1 0 0 1 1-1h3.5a1 1 0 0 1 1 1c0 1.25.2 2.45.57 3.6a1 1 0 0 1-.25 1z"/></svg>
      (555) 017-3391
    </span>
  </div>
  <div class="website">
    <svg viewBox="0 0 24 24"><circle cx="12" cy="12" r="10" fill="none" stroke="#c3d82e" stroke-width="2"/><path d="M2 12h20M12 2c3 3 3 17 0 20M12 2c-3 3-3 17 0 20" fill="none" stroke="#c3d82e" stroke-width="1.6"/></svg>
    <span>www.<span class="green">greenfieldgrounds</span>.com</span>
  </div>

  <div class="accent-bar accent-bar--bottom"></div>
</main>
</body>
</html>
```